Landing page for selling a web application used by archeologists

We are selling a web program that professional archeologists use. This program is developed and designed already. But we are now building another website for presenting this web program.
I have uploaded a pdf file that shows the mockup of the future web page. You will also find a folder containing the photos used in the mockup. You can use your own photos for the ones named with "(can be changed)".
There is another folder called "otherPhoto". You can use them if you want to do background or ambiance...
We expect a really clean, serious, and professional design.

You will see in the mockup that there is a first part (main header) followed by 6 subparts presenting the different aspect of the web app. It finishes with the last part presenting ourselves and inviting to test the program.

Here are some links to website designs that go in the direction of what we want.
https://marovel.quintabrook.com/startup/#home
https://www.pathcrafter-wp. com/mobileapp-landing/
https://en.dravelpoint.com/
https://assets.korinthub.com/en/plyva-saas-software-landing-html5-page-template-RT4WN7/preview

Don't hesitate to contact me if you need more explanations.
As requested by a designer, I also added 2 print screen of the app that we are selling.
Updates

Feel free to use your own photos for background images for example...

Target Market(s)

Professional archaeologists

Industry/Entity Type

Archeology

Number of Pages Required

1 page

Colors
0054AA
0677BA
7BADD7
CADEEF
E8F1F8
0094D4
00A9DD
6FCCEA
C7EBF8
E9F6FB
FFC000
F8CF3A
FAE287
FDF2CF
FEFAEE

Requirements
Must have
• A professional look that says that our company is large and serious

```html
<!DOCTYPE html>
<html lang="en">
<head>
<meta charset="utf-8">
<title>StrataCore – Technology Serving Archeology</title>
<link href="https://fonts.googleapis.com/css2?family=Rubik:wght@300;400;500&display=swap" rel="stylesheet">
<style>
:root{
  --ink:#2b2b2b;
  --ink-soft:#4a4a4a;
  --band:#e6e6e6;
  --white:#ffffff;
  --accent:#4ea8f2;
  --accent-dark:#2f8fe0;
  --nav-active:#d0142c;
  --shield:#3a8fe6;
  --money:#5fd04a;
  --hex:#e8652a;
}
*{box-sizing:border-box;margin:0;padding:0}
html,body{width:1200px;height:3986px;overflow:hidden}
body{font-family:"Rubik",Arial,sans-serif;color:var(--ink);background:var(--white);position:relative}
.section{position:absolute;left:0;width:1200px}
.band{background:var(--band)}
.abs{position:absolute}
.btn{position:absolute;display:flex;align-items:center;justify-content:center;background:var(--accent);color:#fff;font-weight:500;border-radius:16px;box-shadow:0 2px 6px rgba(78,168,242,.35);font-size:13px}
.media{position:absolute}

/* header */
.site-header{top:0;height:139px}
.brand{left:88px;top:44px;font-size:30px;font-weight:300;color:var(--ink);letter-spacing:.3px}
.brand b{font-weight:500}
.nav a{position:absolute;top:54px;font-size:15px;font-weight:500;color:var(--ink);text-decoration:none}
.nav .active{color:var(--nav-active);border-bottom:2px solid var(--nav-active);padding-bottom:3px}
.login{left:1003px;top:50px;display:flex;align-items:center;gap:12px;font-size:15px;font-weight:500}
.login i{display:block;width:26px;height:17px;background:#24418f}

/* hero */
.hero{top:139px;height:336px}
.hero h1{left:88px;top:44px;font-size:40px;font-weight:500;line-height:44px;width:460px}
.hero p{left:87px;top:141px;font-size:15px;line-height:19px;width:240px;color:var(--ink-soft)}
.hero .btn{left:86px;top:218px;width:120px;height:31px}
.hero .media{left:534px;top:-38px;width:588px;height:372px;background:linear-gradient(135deg,#3b4a44,#7d8a76 45%,#c9ccc8 55%,#eceff1);border-radius:6px}

/* modules */
.module h2{position:absolute;font-size:38px;font-weight:500;letter-spacing:.3px}
.module .sub{position:absolute;font-size:16px;color:var(--ink-soft)}
.module .copy{position:absolute;font-size:17px;line-height:23px;color:var(--ink-soft)}

.entry{top:475px;height:465px}
.entry .media{left:80px;top:93px;width:581px;height:302px;background:linear-gradient(160deg,#1c2b33,#2d4b57 60%,#111);border-radius:6px}
.entry h2{left:701px;top:92px;font-size:37px}
.entry .sub{left:701px;top:141px;font-size:15px}
.entry .copy{font-size:15px;line-height:19px;left:701px}
.entry .btn{left:701px;top:340px;width:120px;height:31px}

.analysis{top:940px;height:449px}
.analysis .media{left:608px;top:0;width:465px;height:449px;background:linear-gradient(180deg,#fff 0,#f6efe3 30%,#fff 55%,#eaeaea 100%)}
.analysis h2{left:80px;top:48px;font-size:46px}
.analysis .sub{left:80px;top:110px;font-size:18px}
.analysis .copy{left:80px;font-size:18px;line-height:23px}
.analysis .btn{left:80px;top:343px;width:120px;height:31px}

.view{top:1389px;height:602px}
.view .media{left:31px;top:114px;width:569px;height:379px;background:linear-gradient(180deg,#8fb3d9 0,#c9d8e6 45%,#8c8371 70%,#6f8ea3 100%)}
.view h2{left:666px;top:120px;font-size:46px}
.view .sub{left:666px;top:178px;font-size:18px}
.view .copy{left:666px;font-size:18px;line-height:23px}
.view .btn{left:666px;top:407px;width:120px;height:31px}

.forum{top:1991px;height:450px}
.forum .media{left:574px;top:37px;width:550px;height:377px;background:linear-gradient(135deg,#ffffff,#eef3fb);box-shadow:0 1px 3px rgba(0,0,0,.12)}
.forum h2{left:80px;top:40px;font-size:46px}
.forum .sub{left:80px;top:101px;font-size:18px}
.forum .copy{left:80px;font-size:18px;line-height:23px}
.forum .btn{left:80px;top:333px;width:120px;height:31px}

.archive{top:2441px;height:567px}
.archive .media{left:76px;top:95px;width:484px;height:364px;background:linear-gradient(120deg,#5e6770,#b9b3a4 45%,#e7e6e3 80%,#f4f4f4)}
.archive h2{left:628px;top:92px;font-size:46px}
.archive .sub{left:628px;top:152px;font-size:18px}
.archive .copy{left:628px;font-size:18px;line-height:23px}
.archive .btn{left:628px;top:382px;width:120px;height:31px}

/* about */
.about{top:3008px;height:978px}
.about-band{position:absolute;left:0;top:0;width:1200px;height:405px;background:var(--band)}
.about h3{position:absolute;left:0;width:1200px;top:47px;text-align:center;font-size:22px;font-weight:500}
.about .intro{position:absolute;left:250px;width:700px;top:88px;text-align:center;font-size:14px;line-height:19px;color:var(--ink-soft)}
.card{position:absolute;top:204px;width:299px;height:379px;background:#fff;border-radius:46px;box-shadow:0 2px 8px rgba(0,0,0,.12);text-align:center}
.card svg,.card .dollar{position:absolute;left:50%;transform:translateX(-50%);top:30px}
.card .dollar{font-size:104px;line-height:90px;color:var(--money);font-weight:500}
.card h4{position:absolute;left:20px;right:20px;top:134px;font-size:17px;font-weight:500;line-height:21px}
.card p{position:absolute;left:24px;right:24px;top:199px;font-size:13px;line-height:19.5px;color:var(--ink-soft)}
.about .trial{position:absolute;left:0;width:1200px;top:646px;text-align:center;font-size:24px;font-weight:400}
.about .btn{left:492px;top:727px;width:215px;height:58px;border-radius:29px;font-size:23px}
</style>
</head>
<body>

<header class="section site-header">
  <div class="abs brand">Strata<b>Core</b></div>
  <nav class="nav">
    <a class="active" style="left:584px" href="#solution">Solution</a>
    <a style="left:714px" href="#price">Price</a>
    <a style="left:822px" href="#contact">Contact</a>
  </nav>
  <div class="abs login"><i></i>Login</div>
</header>

<section class="section band hero">
  <h1 class="abs">Technology Serving Archeology</h1>
  <p class="abs">StrataCore the solution to input, analyse and promote the archaeological heritage</p>
  <a class="btn">Get Started</a>
  <div class="media" role="img" aria-label="Two desktop screens showing the StrataCore application with a site map and a data entry form"></div>
</section>

<section class="section module entry" id="solution">
  <div class="media" role="img" aria-label="Television screen and tablet displaying the archaeological units table of StrataEntry"></div>
  <h2>StrataEntry</h2>
  <div class="sub">Capture of archaeological information</div>
  <div class="copy" style="top:208px;width:400px">How to make more, faster, with the same amount of resources ?</div>
  <div class="copy" style="top:293px">-&gt; StrataCore as force multiplier</div>
  <a class="btn">More details</a>
</section>

<section class="section band module analysis">
  <h2>StrataAnalysis</h2>
  <div class="sub">Analysis of archaeological information</div>
  <div class="copy" style="top:180px;width:450px">How to detect hidden relationships, make sense of the information and preserve the big picture?</div>
  <div class="copy" style="top:249px;width:380px">-&gt; StrataCore as an intuitive solution to complex analysis problems</div>
  <a class="btn">More details</a>
  <div class="media" role="img" aria-label="Analysis charts: a clustered heat map, a correspondence analysis scatter plot and line charts of archaeological discoveries by period"></div>
</section>

<section class="section module view">
  <div class="media" role="img" aria-label="Photograph of a medieval lakeside castle under a cloudy sky"></div>
  <h2>StrataView</h2>
  <div class="sub">Promotion of the archaeological heritage</div>
  <div class="copy" style="top:225px;width:450px">How to render the archaeological heritage accessible to the general public, as well as to the educational and tourist sectors?</div>
  <div class="copy" style="top:317px;width:340px">-&gt; StrataCore as a mobilizing and unifying power</div>
  <a class="btn">More details</a>
</section>

<section class="section band module forum">
  <h2>StrataForum</h2>
  <div class="sub">Staying in touch with the community</div>
  <div class="copy" style="top:147px;width:460px">How to connect among specialists and exchange ideas across borders and languages ?</div>
  <div class="copy" style="top:236px;width:440px">-&gt; StrataForum as a solution for multilingual specialist networking</div>
  <a class="btn">More details</a>
  <div class="media" role="img" aria-label="Illustration of a network of connected community members"></div>
</section>

<section class="section module archive">
  <div class="media" role="img" aria-label="Photograph of tall stacks of paper files and binders"></div>
  <h2>StrataArchive</h2>
  <div class="sub">Retrieval of information</div>
  <div class="copy" style="top:214px;width:470px">How to fnd information quickly within archives in various formats (pdf, xls, doc, etc.) ?</div>
  <div class="copy" style="top:290px">-&gt; StrataCore as a solution for dispersed information</div>
  <a class="btn">More details</a>
</section>

<section class="section about" id="contact">
  <div class="about-band"></div>
  <h3>StrataCore: innovative, reliable, at the cutting edge of technology</h3>
  <p class="intro">Founded by a Swiss team of computer engineers and statistical analysts, StrataCore places innovation at the service of success. Its vocation: to ofer the latest computer tools to the world of archaeology in order to facilitate and promote the work of archaeologists</p>

  <div class="card" style="left:132px">
    <svg width="70" height="82" viewBox="0 0 70 82" aria-hidden="true">
      <path d="M35 2 L68 12 V40 C68 62 52 75 35 80 C18 75 2 62 2 40 V12 Z" fill="var(--shield)"/>
      <path d="M35 10 V41 H61 C60 58 48 68 35 72 Z" fill="#fff"/>
      <path d="M35 10 L9 18 V41 H35 Z" fill="#fff"/>
    </svg>
    <h4>The expertise and security<br>of a Swiss company</h4>
    <p>We bring together the most advanced technical engineering skills to deploy the right solutions for the most demanding problems.<br>Big data input and processing, scalability, statistic analysis, deep learning, machine learning are our daily routine</p>
  </div>

  <div class="card" style="left:450px">
    <div class="dollar" aria-hidden="true">$</div>
    <h4>Affordable prices</h4>
    <p>Budgets in archaeology are often limited. Reaching a large number of users allows advanced technological services that are usually very expensive to be ofered at very low prices.</p>
  </div>

  <div class="card" style="left:771px">
    <svg width="92" height="80" viewBox="0 0 92 80" aria-hidden="true" fill="none" stroke="var(--hex)" stroke-width="3">
      <polygon points="24,4 68,4 90,40 68,76 24,76 2,40"/>
      <polygon points="46,10 76,40 46,70 16,40" stroke-width="2"/>
      <line x1="24" y1="4" x2="68" y2="76" stroke-width="2"/>
      <line x1="68" y1="4" x2="24" y2="76" stroke-width="2"/>
      <line x1="2" y1="40" x2="90" y2="40" stroke-width="2"/>
    </svg>
    <h4>Ongoing developments</h4>
    <p>Accompanied by professional archaeologists, we are continually shaping StrataCore to meet their precise needs and expectations.<br>We are always listening to new development proposals in order to solve the problems that archeologists from all countries have in common.</p>
  </div>

  <div class="trial">Get now a free 3-month trial of StrataCore</div>
  <a class="btn">Contact Us</a>
</section>

</body>
</html>
```